We are in search of a new business card design for our business. We have a Mexican Grocery Store called Tortilla Grove Market, we would like to see that some have mexican design, but we are open to any type of designs.

Phone: to be announced
Fax: to be announced

Address is:
2415 Calloway Blvd
Fernhollow, MD 21990

```html
<!DOCTYPE html>
<html lang="en">
<head>
<meta charset="utf-8">
<title>Tortilla Grove Market – Business Card</title>
<link rel="stylesheet" href="https://fonts.googleapis.com/css2?family=Arimo:wght@400;700&display=swap">
<style>
  :root {
    --backdrop: #9b9b9b;
    --card: #f4f4f3;
    --ink: #1c1c1c;
    --text: #3a3a3a;
    --muted: #5a5a5a;
    --rule: #6a6a6a;
  }
  * { margin: 0; padding: 0; box-sizing: border-box; }
  html, body { width: 1200px; height: 1200px; overflow: hidden; }
  body {
    background: var(--backdrop);
    font-family: "Arimo", Arial, sans-serif;
    position: relative;
  }
  .card {
    position: absolute;
    left: 100px; top: 314px;
    width: 1000px; height: 572px;
    background: var(--card);
    box-shadow: 0 14px 40px rgba(0,0,0,0.25);
  }
  .brand {
    position: absolute;
    left: 60px; top: 0; bottom: 0;
    width: 360px;
    display: flex; align-items: center; gap: 18px;
  }
  .brand-dot {
    flex: none;
    width: 38px; height: 38px;
    border-radius: 50%;
    background: var(--ink);
  }
  .brand-name {
    font-weight: 700;
    font-size: 44px;
    line-height: 1.1;
    color: var(--ink);
  }
  .divider {
    position: absolute;
    left: 460px; top: 70px; bottom: 70px;
    width: 1.5px;
    background: var(--rule);
  }
  .person {
    position: absolute;
    left: 500px; top: 82px;
  }
  .person-name { font-size: 44px; color: var(--text); }
  .person-role { font-size: 26px; color: var(--muted); margin-top: 4px; }
  .contacts {
    position: absolute;
    left: 500px; bottom: 82px;
    list-style: none;
    display: flex; flex-direction: column; gap: 14px;
  }
  .contact {
    display: flex; align-items: center; gap: 14px;
    font-size: 22px; color: var(--text);
    white-space: nowrap;
  }
  .contact-icon {
    flex: none;
    width: 24px; height: 24px;
    background: var(--ink);
    border-radius: 3px;
    display: flex; align-items: center; justify-content: center;
  }
  .contact-icon svg { width: 16px; height: 16px; fill: var(--card); }
</style>
</head>
<body>
  <section class="card" aria-label="Tortilla Grove Market business card">
    <div class="brand">
      <span class="brand-dot"></span>
      <span class="brand-name">Tortilla Grove Market</span>
    </div>
    <div class="divider"></div>
    <div class="person">
      <p class="person-name">Dana Whitfield</p>
      <p class="person-role">Owner</p>
    </div>
    <ul class="contacts">
      <li class="contact">
        <span class="contact-icon"><svg viewBox="0 0 16 16"><path d="M4 1.5l2.5 3-1.5 1.5c.8 1.8 2.2 3.2 4 4l1.5-1.5 3 2.5-1.5 2.5C7 13.5 2.5 9 1.5 4z"/></svg></span>
        <span>555.014.2290</span>
      </li>
      <li class="contact">
        <span class="contact-icon"><svg viewBox="0 0 16 16"><rect x="4" y="1.5" width="8" height="4"/><rect x="2" y="6.5" width="12" height="6" rx="1"/><rect x="4" y="10" width="8" height="4.5"/></svg></span>
        <span>555-014-7731</span>
      </li>
      <li class="contact">
        <span class="contact-icon"><svg viewBox="0 0 16 16"><path d="M8 1a5 5 0 0 1 5 5c0 3.5-5 9-5 9S3 9.5 3 6a5 5 0 0 1 5-5zm0 3a2 2 0 1 0 0 4 2 2 0 0 0 0-4z"/></svg></span>
        <span>2415 Calloway Blvd Fernhollow, MD 21990</span>
      </li>
    </ul>
  </section>
</body>
</html>
```